Rooted Ready Rising: Quiet Roots, Open Doors, Steady Hands

I want a modern and clean looking book cover. 5.25x8

Title
Rooted Ready Rising

Subtitle
Quiet Roots, Open Doors, Steady Hands

I don’t just want a graphic, I want it to make sense. If it can just be the words and a textured looking background, I’ll be ok with that too. I just want it to look crisp, clean, modern.

I want the back to have my book blurb and bio attached with the pic that’s attached.

Target Market(s)

Self help

Requirements
Must have
• Modern, clean look, look professional, attract customers.

```html
<!DOCTYPE html>
<html lang="en">
<head>
<meta charset="utf-8">
<title>Rooted Ready Rising – Back Cover</title>
<link href="https://fonts.googleapis.com/css2?family=Arimo:ital,wght@0,400;0,700;1,700&display=swap" rel="stylesheet">
<style>
  :root {
    --paper: #cdc6c1;
    --paper-light: #d3ccc7;
    --ink: #1c1a19;
    --photo-bg: #e4e3e3;
  }
  html, body {
    margin: 0;
    padding: 0;
    overflow: hidden;
  }
  body {
    width: 788px;
    height: 1200px;
  }
  .back-cover {
    position: relative;
    width: 788px;
    height: 1200px;
    overflow: hidden;
    background: radial-gradient(ellipse at 40% 30%, var(--paper-light), var(--paper) 70%);
    color: var(--ink);
    font-family: "Arimo", Arial, sans-serif;
    font-size: 18px;
    line-height: 24.75px;
    letter-spacing: -0.15px;
  }
  .book-heading {
    position: absolute;
    left: 44px;
    top: 62px;
    margin: 0;
    font-size: 20px;
    font-weight: 700;
    line-height: 28px;
  }
  .blurb {
    position: absolute;
    left: 44px;
    top: 104px;
    width: 690px;
  }
  .blurb p,
  .bio p {
    margin: 0 0 4px;
    text-align: justify;
  }
  .blurb .lead {
    margin-bottom: 16px;
    text-align: left;
  }
  .book-title {
    font-weight: 700;
    font-style: italic;
  }
  .author-photo {
    position: absolute;
    left: 44px;
    top: 608px;
    width: 155px;
    height: 219px;
    background: var(--photo-bg);
  }
  .bio-side {
    position: absolute;
    left: 223px;
    top: 606px;
    width: 511px;
  }
  .bio-full {
    position: absolute;
    left: 44px;
    top: 843px;
    width: 690px;
  }
</style>
</head>
<body>
<main class="back-cover">
  <h1 class="book-heading">Rooted Ready Rising</h1>

  <section class="blurb">
    <p class="lead">Everyone has big dreams and lofty goals, but few give themselves permission to try.</p>
    <p><span class="book-title">Rooted Ready Rising: Quiet Roots, Open Doors, Steady Hands</span> is for anyone who has ever been stymied by negative self-talk, maltreatment, troubles at home, relationship problems, or has experienced anything significant that has made you want to abandon your dreams.</p>
    <p>Part memoir, part self-help book, part spiritual guide, this book aims to provide encouragement and a helping hand to anyone who feels like life has passed them by or think their time will never come.</p>
    <p>Inside, you’ll find deeply personal stories and anecdotes from Author Renee Walcott. Her personal experiences provide a detailed account and roadmap for how to lift yourself out of a dark spot, find your voice, dream bigger, dare to try, and change your life for the better.</p>
    <p>If you’ve ever felt like where you are now is where you’ll always be or fear that your prayers will never be answered, this book will help you move past obstacles, shatter expectations, and learn how to confidently bet on yourself because you’re worth it.</p>
    <p>Scroll up and click “Order Your Copy” to find the support and motivation you need to move forward in life and finally be who you were meant to be!</p>
  </section>

  <svg class="author-photo" role="img" aria-label="Author portrait: standing woman in a black slogan t-shirt, white jeans and red heels on a light grey backdrop" viewBox="0 0 155 219" preserveAspectRatio="none">
    <defs>
      <linearGradient id="portrait-tone" x1="0" y1="0" x2="0" y2="1">
        <stop offset="0" stop-color="#e6e5e5"/>
        <stop offset="0.5" stop-color="#d9d6d5"/>
        <stop offset="1" stop-color="#e6e5e5"/>
      </linearGradient>
    </defs>
    <rect width="155" height="219" fill="url(#portrait-tone)"/>
  </svg>

  <section class="bio bio-side">
    <p>Renee Walcott is a helper. For as long as she can remember, she’s always wanted to do the right thing, but life, circumstance, and some very tough years, set her on a path that conflicted with what was in her heart... until something clicked and she made herself and her goals a priority.</p>
    <p>A dreamer and visionary at her core, she knows all too well how much faith and courage it takes to defy expectations and build your own path forward. Her tenacity led her in a direction that would change her life for the better.</p>
  </section>

  <section class="bio bio-full">
    <p>After being told she wasn’t “college material” in high school, she made it her mission to never allow anyone to define who she is, and more importantly, to empower others to do the same. Today, the devout Christian, Author, Motivator, Coach, Educator, and Educational Leader, holds 3 degrees (Bachelors of Science in Psychology, Master of Education, and Educational Specialist) and is currently in the dissertation phase of a Doctorate of Education. Recently, she added Life Coach to her resume.</p>
    <p>When she’s not teaching, studying, coaching, reading, writing, listening to music, or helping others achieve their goals, she spends as much time as she can with her loving husband, three beautiful daughters, her college aged God-daughter, and countless friends.</p>
  </section>
</main>
</body>
</html>
```